National Dart League Needs a Graphic Design

We need a graphic design for an established company named 'TripleFern' for our national (US) singles dart league. We now have hundreds of players in multiple states.

Our league is based on international long format darts (see KWN, TLM) and provides our members with the ability to participate with other players in other states. We have regional playoffs and offer sponsorships for our playoff winners to large dart tournaments.

We're looking for an image that showcases the national scope of our league and is suitable for social media campaigns. This will be used to market our league to new areas.

Industry/Entity Type

Graphic Design

```html
<!DOCTYPE html>
<html lang="en">
<head>
<meta charset="utf-8">
<title>National (US) Singles Dart League</title>
<link rel="stylesheet" href="https://fonts.googleapis.com/css2?family=Anton&family=Tulpen+One&display=swap">
<style>
  :root {
    --page-bg: #2b2b2e;
    --banner-dark: #07090f;
    --glow-blue: #1f6fd6;
    --deep-blue: #0a1d3f;
    --glow-red: #b3141c;
    --deep-red: #3a0a10;
    --text-white: #ffffff;
    --logo-panel: #ffffff;
    --logo-ink: #3a3a3a;
  }
  * { margin: 0; padding: 0; box-sizing: border-box; }
  html, body {
    width: 1200px;
    height: 694px;
    overflow: hidden;
    background: var(--page-bg);
  }
  .banner {
    position: absolute;
    left: 124px;
    top: 108px;
    width: 951px;
    height: 476px;
    overflow: hidden;
    background: var(--banner-dark);
  }
  .cover-art {
    position: absolute;
    inset: 0;
    background:
      radial-gradient(ellipse 200px 160px at 420px 250px, rgba(255,255,255,0.45), transparent 75%),
      radial-gradient(ellipse 380px 300px at 330px 90px, rgba(31,111,214,0.6), transparent 75%),
      radial-gradient(ellipse 460px 360px at 720px 120px, rgba(179,20,28,0.7), transparent 75%),
      linear-gradient(100deg, var(--deep-blue) 0%, var(--banner-dark) 45%, var(--deep-red) 100%);
  }
  .logo-panel {
    position: absolute;
    left: 541px;
    top: 35px;
    width: 372px;
    height: 80px;
    background: var(--logo-panel);
    display: flex;
    align-items: center;
    justify-content: center;
  }
  .logo-name {
    font-family: "Anton", sans-serif;
    font-size: 34px;
    letter-spacing: 2px;
    color: var(--logo-ink);
  }
  .headline {
    position: absolute;
    display: block;
    left: 541px;
    width: 375px;
    color: var(--text-white);
    text-align: center;
    line-height: 1;
    font-weight: 400;
    white-space: nowrap;
  }
  .headline--national {
    top: 113px;
    font-family: "Anton", sans-serif;
    font-size: 65px;
    letter-spacing: 3px;
    text-indent: 3px;
  }
  .headline--singles {
    top: 152px;
    font-family: "Tulpen One", sans-serif;
    font-size: 150px;
    letter-spacing: 6px;
    text-indent: 6px;
    transform: scale(1.27, 1.84);
    transform-origin: top center;
  }
  .headline--league {
    top: 380px;
    font-family: "Anton", sans-serif;
    font-size: 68px;
    letter-spacing: 4px;
    text-indent: 4px;
  }
</style>
</head>
<body>
  <main class="banner">
    <div class="cover-art" role="img" aria-label="Photograph of a red, white and blue dartboard with a dart striking the bullseye in a burst of light"></div>

    <div class="logo-panel">
      <span class="logo-name">TripleFern</span>
    </div>

    <h1>
      <span class="headline headline--national">NATIONAL (US)</span>
      <span class="headline headline--singles">SINGLES</span>
      <span class="headline headline--league">DART LEAGUE</span>
    </h1>
  </main>
</body>
</html>
```